Pest control srevice Special offer

Pest control to promote our service program. 3 month pest control service for $125.00 Includes svc for ants,bees,wasps,silverfish,rats,mice,roaches. No long term contracts Our customers can purchase the service 3 months at a time as needed throughout the year. Or sign up for the full year at 425.00

Target Market(s)

Home Owners

Industry/Entity Type

Pest Control

Font styles to use
Sans Serif

Requirements
Must have
• must be relevant to pest control see our web site at harlowbugandrodentguard.com
Nice to have
• I want the post card to be laid out in a way that describes our service simple and professional. The program that we are offering really works well for our customers and makes sense they only pay for service when they are having an issue
Should not have
• I don't want pictures of insects that scare people off or unsettling to look at

```html
<!DOCTYPE html>
<html lang="en">
<head>
<meta charset="UTF-8">
<title>Harlow Bug &amp; Rodent Guard – 3 Month Pest Control Special</title>
<link rel="stylesheet" href="https://fonts.googleapis.com/css2?family=Oswald:wght@400;500;600;700&family=Roboto:wght@500;700&display=swap">
<style>
  :root {
    --white: #ffffff;
    --ink: #111111;
    --promo-red: #e2231a;
    --offer-yellow: #ffd21f;
    --band-gold: #c9a02a;
    --terms-grey: #333333;
    --footer-black: #0d0d0d;
    --photo-dark: #2a1606;
    --photo-amber: #b8660f;
    --photo-gold: #f2b43a;
  }
  * { margin: 0; padding: 0; box-sizing: border-box; }
  html, body { width: 1200px; height: 900px; overflow: hidden; background: var(--white); }
  .postcard {
    position: relative;
    width: 1200px;
    height: 900px;
    font-family: "Oswald", sans-serif;
    overflow: hidden;
  }

  /* Header */
  .header {
    position: absolute; left: 0; top: 0;
    width: 1200px; height: 132px;
    background: var(--white);
  }
  .brand {
    position: absolute; left: 20px; top: 30px;
    display: flex; align-items: center; gap: 12px;
  }
  .brand-mark {
    width: 22px; height: 22px;
    background: var(--ink);
  }
  .brand-name {
    font-family: "Oswald", sans-serif;
    font-weight: 600;
    font-size: 26px;
    line-height: 1.05;
    color: var(--ink);
    text-transform: uppercase;
    letter-spacing: 0.5px;
  }
  .call-to-action {
    position: absolute; right: 16px; top: 16px;
    text-align: right;
  }
  .call-label {
    font-weight: 600;
    font-size: 30px;
    line-height: 1.1;
    color: var(--ink);
    text-transform: uppercase;
  }
  .call-phone {
    font-weight: 600;
    font-size: 56px;
    line-height: 1.05;
    color: var(--promo-red);
    letter-spacing: 0.5px;
  }

  /* Hero photo area */
  .hero-photo {
    position: absolute; left: 0; top: 132px;
    width: 1200px; height: 483px;
    background:
      radial-gradient(ellipse at 40% 85%, var(--photo-gold) 0%, var(--photo-amber) 30%, transparent 60%),
      radial-gradient(ellipse at 30% 40%, #6b3a0c 0%, transparent 55%),
      linear-gradient(180deg, var(--photo-dark) 0%, #4a2608 55%, var(--photo-amber) 100%);
  }

  /* Price starburst */
  .price-burst {
    position: absolute; left: 845px; top: 193px;
    width: 350px; height: 350px;
  }
  .price-burst svg { width: 100%; height: 100%; display: block; }
  .price-text {
    position: absolute; left: 845px; top: 193px;
    width: 350px; height: 350px;
    display: flex; flex-direction: column; align-items: center; justify-content: center;
    text-align: center;
  }
  .price-amount {
    font-weight: 600;
    font-size: 112px;
    line-height: 0.95;
    color: var(--white);
  }
  .price-amount .currency {
    font-size: 52px;
    vertical-align: 42px;
    margin-right: 2px;
  }
  .price-term {
    font-weight: 700;
    font-size: 48px;
    line-height: 1.05;
    color: var(--offer-yellow);
    text-transform: uppercase;
  }
  .price-service {
    font-weight: 600;
    font-size: 20px;
    line-height: 1.3;
    color: var(--white);
    text-transform: uppercase;
  }

  /* Services band */
  .services-band {
    position: absolute; left: 0; top: 615px;
    width: 1200px; height: 90px;
    background: var(--band-gold);
    display: flex; align-items: center; justify-content: center;
  }
  .services-list {
    font-weight: 600;
    font-size: 33px;
    color: var(--ink);
    text-transform: uppercase;
    white-space: pre;
    letter-spacing: 0.3px;
  }

  /* Terms */
  .terms {
    position: absolute; left: 0; top: 705px;
    width: 1200px; height: 123px;
    background: var(--terms-grey);
    display: flex; align-items: center; justify-content: center;
    padding: 0 30px;
  }
  .terms-copy {
    font-weight: 500;
    font-size: 25px;
    line-height: 1.65;
    color: var(--white);
    text-align: center;
    text-transform: uppercase;
    letter-spacing: 0.4px;
  }

  /* Footer */
  .footer {
    position: absolute; left: 0; top: 828px;
    width: 1200px; height: 72px;
    background: var(--footer-black);
    display: flex; align-items: center; justify-content: center;
    font-family: "Roboto", sans-serif;
    font-weight: 500;
    font-size: 23px;
    color: var(--white);
    white-space: pre;
  }
</style>
</head>
<body>
  <main class="postcard">
    <header class="header">
      <div class="brand">
        <span class="brand-mark"></span>
        <span class="brand-name">Harlow Bug<br>&amp; Rodent Guard</span>
      </div>
      <div class="call-to-action">
        <p class="call-label">Call for a free estimate!</p>
        <p class="call-phone">800-555-0178</p>
      </div>
    </header>

    <section class="hero-photo" role="img" aria-label="Warm close-up photo of honeybees working on golden honeycomb"></section>

    <div class="price-burst" aria-hidden="true">
      <svg viewBox="-175 -175 350 350">
        <polygon fill="var(--promo-red)" points="170,0 142.8,25.2 159.8,58.1 125.6,72.5 130.2,109.3 93.2,111.1 85,147.2 49.6,136.3 29.6,167.5 0,145 -29.6,167.5 -49.6,136.3 -85,147.2 -93.2,111.1 -130.2,109.3 -125.6,72.5 -159.8,58.1 -142.8,25.2 -170,0 -142.8,-25.2 -159.8,-58.1 -125.6,-72.5 -130.2,-109.3 -93.2,-111.1 -85,-147.2 -49.6,-136.3 -29.6,-167.5 0,-145 29.6,-167.5 49.6,-136.3 85,-147.2 93.2,-111.1 130.2,-109.3 125.6,-72.5 159.8,-58.1 142.8,-25.2"/>
      </svg>
    </div>
    <div class="price-text">
      <p class="price-amount"><span class="currency">$</span>125</p>
      <p class="price-term">3 Months</p>
      <p class="price-service">Pest Control Service</p>
    </div>

    <section class="services-band">
      <p class="services-list">Includes svc for  ants,bees,wasps,silverfish, rats mice,roaches</p>
    </section>

    <section class="terms">
      <p class="terms-copy">No long term contracts our customers can purchase the service 3 months at a time as needed throughout the year. Or sign up for the full year at 425.00</p>
    </section>

    <footer class="footer">27 Linden Avenue Pittsburgh, PA 15209  • Our Website : www.harlowbugandrodentguard.com</footer>
  </main>
</body>
</html>
```